Legal Campaign

A courier compavny that offer Legal services like filing/recording Court documents.

These info must be on card: Can We Help With Your Legal Services? Need Your Court documents quickly filed? .Filing/Recording in Erie, Niagara & Monroe County .Pick-up within 15-30 minutes of call .Medical records pick-up & delivery .Court-Authorized Process Servers .$9.00 Buffalo to Buffalo .Volume Discounts Call Liam Torvane@716-555-0148 The address must be 47 Harlow Ave., Buffalo NY 14209

Please add the following info: 1.Post Office Pickup/Deliveries 2. Liamtorvane@brisktrn.com

Target Market(s)

Law firms & legal community.

Industry/Entity Type

Court

Requirements
Must have
• SwiftHaulo logo must be on card. Please visit the website@brisktrn.com to check out the logo. Thanks

```html
<!DOCTYPE html>
<html lang="en">
<head>
<meta charset="utf-8">
<title>SwiftHaulo Couriers – Legal Services</title>
<link href="https://fonts.googleapis.com/css2?family=Open+Sans:ital,wght@0,400;0,600;0,700;1,700&display=swap" rel="stylesheet">
<style>
  :root {
    --blue: #1a5aa6;
    --orange: #f7931e;
    --ink: #3d4248;
    --text: #2f3338;
    --paper: #ffffff;
    --page: #eeeeee;
    --art-light: #e6e8ec;
    --art-mid: #c9cfd8;
  }
  * { margin: 0; padding: 0; box-sizing: border-box; }
  html, body { width: 1200px; height: 948px; overflow: hidden; background: var(--page); }
  .card {
    position: relative; width: 1200px; height: 948px; background: var(--paper);
    font-family: "Open Sans", Arial, sans-serif; color: var(--text); overflow: hidden;
  }
  .top-stripe { position: absolute; left: 0; top: 0; width: 1200px; height: 16px; }
  .headline {
    position: absolute; font-style: italic; font-weight: 700; font-size: 38px;
    color: var(--ink); white-space: nowrap; line-height: 1;
  }
  .headline-help { left: 33px; top: 60px; }
  .headline-court { right: 40px; top: 142px; }
  .accent-orange { color: var(--orange); }
  .accent-blue { color: var(--blue); }
  .offer-title { position: absolute; left: 33px; top: 240px; font-size: 32px; font-weight: 600; color: var(--ink); }
  .offer-list { position: absolute; left: 50px; top: 306px; list-style: none; }
  .offer-list li {
    position: relative; padding-left: 26px; font-size: 27px; line-height: 1;
    height: 66px; color: var(--text); white-space: nowrap;
  }
  .offer-list li::before {
    content: ""; position: absolute; left: 0; top: 11px; width: 10px; height: 10px;
    border-radius: 50%; background: var(--blue);
  }
  .files-art {
    position: absolute; left: 720px; top: 280px; width: 400px; height: 420px;
    border-radius: 42% 38% 30% 34%;
    background: radial-gradient(circle at 50% 45%, var(--art-mid), var(--art-light) 70%);
  }
  .brand { position: absolute; left: 33px; top: 775px; display: flex; align-items: center; gap: 14px; }
  .brand-mark { width: 34px; height: 34px; background: var(--orange); }
  .brand-name { font-size: 50px; font-weight: 700; color: var(--blue); line-height: 1; }
  .contact-note {
    position: absolute; right: 40px; top: 728px; text-align: right;
    font-size: 31px; line-height: 44px; color: var(--text);
  }
  .contact-email { font-size: 26px; color: var(--blue); }
  .footer-bar { position: absolute; left: 0; bottom: 0; width: 1200px; height: 74px; }
  .footer-bg { position: absolute; left: 0; top: 0; }
  .footer-item {
    position: absolute; top: 0; height: 74px; display: flex; align-items: center; gap: 12px;
    color: #fff; font-size: 30px; font-weight: 700; white-space: nowrap;
  }
  .footer-icon { flex: none; }
  .footer-address { left: 50px; }
  .footer-phone { right: 40px; }
</style>
</head>
<body>
<div class="card">
  <svg class="top-stripe" viewBox="0 0 1200 16" aria-hidden="true">
    <polygon points="0,0 412,0 400,16 0,16" fill="var(--orange)"/>
    <polygon points="412,0 1200,0 1200,16 400,16" fill="var(--blue)"/>
  </svg>

  <h1 class="headline headline-help">Can We Help With Your <span class="accent-orange">Legal Services</span>?</h1>
  <h2 class="headline headline-court">Need Your Court <span class="accent-blue">documents quickly filed</span>?</h2>

  <h3 class="offer-title">We Offer</h3>
  <ul class="offer-list">
    <li>Filing/Recording in Erie, Niagara &amp; Monroe County</li>
    <li>Pick-up within 15-30 minutes of call</li>
    <li>Medical records pick-up &amp; delivery</li>
    <li>Post Office Pickup/Deliveries</li>
    <li>Court-Authorized Process Servers</li>
    <li>$9.00 Buffalo to Buffalo</li>
  </ul>

  <div class="files-art" role="img" aria-label="Illustration of an open ring binder stacked on blue and orange file folders with loose papers"></div>

  <div class="brand">
    <span class="brand-mark"></span>
    <span class="brand-name">SwiftHaulo</span>
  </div>

  <p class="contact-note">Volume Discounts<br>Call Liam Torvane<br><span class="contact-email">Liamtorvane@brisktrn.com</span></p>

  <footer class="footer-bar">
    <svg class="footer-bg" width="1200" height="74" viewBox="0 0 1200 74" aria-hidden="true">
      <polygon points="0,0 790,0 750,74 0,74" fill="var(--blue)"/>
      <polygon points="790,0 1200,0 1200,74 750,74" fill="var(--orange)"/>
    </svg>
    <div class="footer-item footer-address">
      <svg class="footer-icon" width="22" height="30" viewBox="0 0 22 30" aria-hidden="true">
        <path d="M11 1C5.5 1 1 5.4 1 10.9 1 18 11 29 11 29s10-11 10-18.1C21 5.4 16.5 1 11 1z" fill="none" stroke="#fff" stroke-width="2.6"/>
        <circle cx="11" cy="11" r="3.6" fill="#fff"/>
      </svg>
      <span>47 Harlow Ave., Buffalo NY 14209</span>
    </div>
    <div class="footer-item footer-phone">
      <svg class="footer-icon" width="26" height="26" viewBox="0 0 24 24" aria-hidden="true">
        <path d="M6.6 10.8c1.4 2.8 3.8 5.1 6.6 6.6l2.2-2.2c.3-.3.7-.4 1-.2 1.1.4 2.3.6 3.6.6.6 0 1 .4 1 1V20c0 .6-.4 1-1 1C10.6 21 3 13.4 3 4c0-.6.4-1 1-1h3.5c.6 0 1 .4 1 1 0 1.3.2 2.5.6 3.6.1.3 0 .7-.2 1L6.6 10.8z" fill="#fff"/>
      </svg>
      <span>716-555-0148</span>
    </div>
  </footer>
</div>
</body>
</html>
```